TheHarborKeyway.com (Luxury Business Card Design)

I’m looking for assistance with design. I have a clear vision in mind, but I need help translating it into a properly formatted file for print.
Ideally, I’d like to work directly with a designer to communicate my vision and finalize the design in the correct vector format required for submission to a printing company. I already have some examples I've created just need someone with design experience to help me do the finishing touches

Target Market(s)

Real Estate

Industry/Entity Type

Real Estate

Contact Information for Business Card

the name of the company, QR code, my The harbor keyway email. Owner/founder title.

Font styles to use
Decorative
Script

Requirements
Must have
• vector for printing company
Nice to have
• I am set on a black and gold design, and will be using a gold foiling. QR code to be done in a gold foiling or inlay.
Should not have
• wild colors I want black and gold, please see my pdf examples.

```html
<!DOCTYPE html>
<html lang="en">
<head>
<meta charset="utf-8">
<title>The Harbor Keyway — Business Card</title>
<link rel="stylesheet" href="https://fonts.googleapis.com/css2?family=Almendra&family=Crimson+Text:ital@0;1&display=swap">
<style>
  :root {
    --page-bg: #e6e6e6;
    --card-black: #0b0b0b;
    --card-glow: #1a1a1a;
    --gold: #b08d3e;
    --ornament-gold: rgba(176, 141, 62, 0.5);
    --ornament-fade: rgba(176, 141, 62, 0.12);
  }
  * { margin: 0; padding: 0; box-sizing: border-box; }
  html, body { width: 1200px; height: 1200px; overflow: hidden; }
  body {
    background: var(--page-bg);
    position: relative;
    font-family: "Crimson Text", Georgia, serif;
  }
  .card {
    position: absolute;
    left: 169px;
    width: 862px;
    height: 507px;
    overflow: hidden;
  }
  .card--front {
    top: 71px;
    background: radial-gradient(ellipse at 85% 40%, var(--card-glow) 0%, var(--card-black) 60%);
  }
  .card--back {
    top: 631px;
    background: radial-gradient(ellipse at 45% 100%, var(--card-glow) 0%, var(--card-black) 60%);
  }
  .card__frame { position: absolute; left: 0; top: 0; width: 862px; height: 507px; }

  .ornament { position: absolute; }
  .ornament--front {
    left: 62px; top: 60px; width: 388px; height: 344px;
    background: linear-gradient(135deg, var(--ornament-gold) 0%, var(--ornament-fade) 70%);
    clip-path: polygon(0 0, 100% 0, 100% 100px, 112px 100px, 112px 100%, 0 100%);
  }
  .ornament--back {
    left: 409px; top: 56px; width: 382px; height: 363px;
    background: linear-gradient(225deg, var(--ornament-gold) 0%, var(--ornament-fade) 70%);
    clip-path: polygon(0 0, 100% 0, 100% 100%, 267px 100%, 267px 128px, 0 128px);
  }

  .brand {
    font-family: "Almendra", "Times New Roman", serif;
    font-weight: 400;
    color: var(--gold);
    position: absolute;
    white-space: nowrap;
    line-height: 1;
  }
  .brand--front { right: 93px; top: 150px; font-size: 38px; }
  .brand--back  { left: 81px; top: 228px; font-size: 56px; }

  .holder {
    position: absolute; right: 93px; top: 212px;
    text-align: right; color: var(--gold);
  }
  .holder__name { font-style: italic; font-size: 41px; line-height: 1.1; }
  .holder__title { font-size: 20px; margin-top: 2px; }

  .contact {
    position: absolute; right: 96px; top: 338px;
    list-style: none; color: var(--gold); font-size: 20px;
  }
  .contact__item {
    display: flex; align-items: center; justify-content: flex-end;
    height: 32.5px; gap: 12px;
  }
  .contact__icon { width: 16px; height: 16px; fill: var(--gold); }
</style>
</head>
<body>
  <section class="card card--front">
    <svg class="card__frame" viewBox="0 0 862 507" aria-hidden="true">
      <polygon points="54,38 810,38 829,57 829,450 810,469 54,469 35,450 35,57" fill="none" stroke="var(--gold)" stroke-width="2"/>
    </svg>
    <div class="ornament ornament--front" role="img" aria-label="Gold flourish ornament in the top-left corner"></div>
    <h1 class="brand brand--front">The Harbor Keyway</h1>
    <div class="holder">
      <p class="holder__name">Your Name</p>
      <p class="holder__title">Designation</p>
    </div>
    <ul class="contact">
      <li class="contact__item">(123) 123-4567
        <svg class="contact__icon" viewBox="0 0 16 16" aria-hidden="true"><path d="M3.2 1.5l2.3 2.6-1.2 1.8c.9 1.9 2.3 3.3 4.2 4.2l1.8-1.2 2.6 2.3-1.4 2.3C6.6 13.2 2.8 9.4 1 4.5z"/></svg>
      </li>
      <li class="contact__item">info@theharborkeyway.com
        <svg class="contact__icon" viewBox="0 0 16 16" aria-hidden="true"><path d="M1.5 3.5h13v9h-13z M1.5 3.5l6.5 5 6.5-5" stroke="#0b0b0b" stroke-width="1"/></svg>
      </li>
      <li class="contact__item">theharborkeyway.com
        <svg class="contact__icon" viewBox="0 0 16 16" aria-hidden="true"><circle cx="8" cy="8" r="6.5"/><path d="M1.5 8h13M8 1.5c-2.5 3-2.5 10 0 13M8 1.5c2.5 3 2.5 10 0 13" fill="none" stroke="#0b0b0b" stroke-width="1"/></svg>
      </li>
    </ul>
  </section>

  <section class="card card--back">
    <svg class="card__frame" viewBox="0 0 862 507" aria-hidden="true">
      <polygon points="54,38 810,38 829,57 829,450 810,469 54,469 35,450 35,57" fill="none" stroke="var(--gold)" stroke-width="2"/>
    </svg>
    <div class="ornament ornament--back" role="img" aria-label="Gold swirl ornament in the top-right corner"></div>
    <h2 class="brand brand--back">The Harbor Keyway</h2>
  </section>
</body>
</html>
```